Re-design of 3 website slider images

If you visit a website called "www.tallyfern.example" you will see on the Home page a 3 image slider which needs to be re-designed.

See section Quiet Glance for how the game works.
See also the tab "The Ledge@ for some of the Avatar images

The 3 replacement images should represent graphically 3 stages of a relationship that is in need of refreshment or repair.

Stage 1 - boredom, complacency, familiarity
Stage 2 - exploration of trying new things
Stage 3 - a more connected vibrant relationship

The key words are"relationship refreshment"

Target Market(s)

Women in a stale relationship (single or married)

Requirements
Must have
• Must appeal to young, middle and older age groups. Anyone in a relationship.
Must be multi-racial, inclusive of all races
Nice to have
• a photo Montage perhaps
Should not have
• Must not be sentimental or over romantic

```html
<!DOCTYPE html>
<html lang="en">
<head>
<meta charset="utf-8">
<title>Relationship Refreshment – Slider Set</title>
<link rel="stylesheet" href="https://fonts.googleapis.com/css2?family=Open+Sans:wght@700;800&family=Dawning+of+a+New+Day&display=swap">
<style>
  :root {
    --page: #ffffff;
    --ink: #111111;
    --accent: #c8161d;
    --shadow: rgba(0, 0, 0, 0.55);
    --bed-light: #f4f3f1;
    --bed-mid: #e2ded9;
    --skin: #d9b49a;
    --sky: #a9c6dc;
    --sea: #6fa8b8;
    --sand: #e8dccb;
    --linen: #f1eeea;
    --wood: #c9a27a;
  }
  html, body {
    margin: 0;
    padding: 0;
    width: 840px;
    height: 1200px;
    overflow: hidden;
    background: var(--page);
  }
  .canvas {
    position: relative;
    width: 840px;
    height: 1200px;
    background: var(--page);
    font-family: "Open Sans", Arial, sans-serif;
    color: var(--ink);
  }
  .slide {
    position: absolute;
    background: var(--page);
    box-shadow: 7px 7px 6px var(--shadow);
    overflow: hidden;
  }
  .slide--stale   { left: 36px; top: 102px; width: 780px; height: 296px; }
  .slide--explore { left: 32px; top: 440px; width: 779px; height: 297px; }
  .slide--connect { left: 35px; top: 792px; width: 777px; height: 298px; }

  .slide__photo { position: absolute; top: 0; }
  .slide--stale .slide__photo {
    left: 18px; top: 50px; width: 336px; height: 246px;
    background: radial-gradient(ellipse at 35% 45%, var(--skin) 0%, var(--bed-mid) 30%, var(--bed-light) 60%, #ffffff 100%);
  }
  .slide--explore .slide__photo {
    left: 0; width: 360px; height: 297px;
    background:
      linear-gradient(to right, rgba(255,255,255,0) 70%, #ffffff 100%),
      linear-gradient(to bottom, var(--sky) 0%, #cfe0ec 45%, var(--sea) 52%, var(--sea) 62%, var(--sand) 75%, var(--sand) 100%);
  }
  .slide--connect .slide__photo {
    left: 0; width: 375px; height: 298px;
    background:
      linear-gradient(to right, rgba(255,255,255,0) 65%, #ffffff 100%),
      radial-gradient(ellipse at 45% 60%, var(--skin) 0%, var(--linen) 40%, #ffffff 80%),
      linear-gradient(to right, var(--linen), var(--wood) 55%, var(--linen) 65%);
  }

  .slide__kicker {
    position: absolute;
    left: 28px; top: 6px;
    margin: 0;
    font-size: 26px;
    font-weight: 700;
    color: var(--accent);
    letter-spacing: 0.2px;
  }
  .slide__headline {
    position: absolute;
    margin: 0;
    font-weight: 700;
    line-height: 1.3;
  }
  .slide--stale .slide__headline   { left: 360px; top: 40px; font-size: 22px; }
  .slide--explore .slide__headline { left: 358px; top: 30px; font-size: 22px; }
  .slide--connect .slide__headline { left: 356px; top: 32px; font-size: 27px; line-height: 1.35; }
  .accent { color: var(--accent); }

  .slide__tagline {
    position: absolute;
    right: 14px;
    margin: 0;
    font-family: "Dawning of a New Day", cursive;
    font-size: 25px;
    white-space: nowrap;
  }
  .slide--stale .slide__tagline   { top: 170px; right: 12px; }
  .slide--explore .slide__tagline { top: 205px; right: 14px; }
  .slide--connect .slide__tagline { top: 205px; right: 18px; }
</style>
</head>
<body>
<main class="canvas">
  <section class="slide slide--stale">
    <div class="slide__photo" role="img" aria-label="Couple lying back to back in white bed sheets, turned away from each other"></div>
    <h1 class="slide__kicker">relationship refreshment</h1>
    <p class="slide__headline">If you gave your Partner 2 hours<br>of <span class="accent">uninterrupted time</span> to spend<br>in any way?</p>
    <p class="slide__tagline">The game that's enjoyable and intimate</p>
  </section>

  <section class="slide slide--explore">
    <div class="slide__photo" role="img" aria-label="Laughing couple in sun hats on a beach, one carrying the other piggyback"></div>
    <p class="slide__headline">Re-capture the <span class="accent">fun</span> of your<br>relationship. Every day is a new<br>chance to refresh.</p>
    <p class="slide__tagline">Learn new things about yourself &amp; your partner</p>
  </section>

  <section class="slide slide--connect">
    <div class="slide__photo" role="img" aria-label="Two pairs of bare feet intertwined at the end of a white bed"></div>
    <p class="slide__headline">The game where the<br><span class="accent">relationship</span> always wins!</p>
    <p class="slide__tagline">Isn't that what you want?</p>
  </section>
</main>
</body>
</html>
```